Theatre Event Email Invite - Gold Lion over Theatre Interior (Reference images attached)

I need an email invitation to my theatre event.

Design:
Please design a graphic gold lion mask similar to the image attached.
Place it over the red image attached of the theatre's interior
Place the following text over it, in gold font:

"
December 15, 2015 at 7 PM
You are cordially invited to an innovative theatrical experience.

FORSAKING THE HERON
Winner of the KRW's “Open-Horizons”Global Scriptwriting Prize
Written and directed by Marla Quistend

Hosted by the Gallery Of Harmony
4152 East Varlo Ave, Los Angeles, CA 90217 "

Industry/Entity Type

Movie Theater

Font styles to use
Serif

Requirements
Must have
• The lion mask graphic
• An image of the theatre interior. If you use one other than the red one, please edit to look tinted red.
Nice to have
• jewel tones including gold and burgundy
• dramatic
Should not have
• not be scary or depressing

```html
<!DOCTYPE html>
<html lang="en">
<head>
<meta charset="utf-8">
<title>Forsaking the Heron — Invitation</title>
<link rel="stylesheet" href="https://fonts.googleapis.com/css2?family=Cinzel:wght@500;600&family=Tinos:wght@400;700&display=swap">
<style>
  :root {
    --burgundy: #6e1420;
    --burgundy-deep: #4a0c15;
    --maroon-ink: #4e1218;
    --gold-light: #f6e3a1;
    --gold: #d9b45e;
    --gold-deep: #a47a2c;
    --gold-text: #f0d488;
    --teal-dark: #0f2a33;
    --teal: #1f5360;
    --seat-red: #5c1c1c;
  }
  html, body {
    margin: 0;
    padding: 0;
    width: 859px;
    height: 1200px;
    overflow: hidden;
    background: #1a0a0d;
  }
  .invite {
    position: relative;
    width: 859px;
    height: 1200px;
    overflow: hidden;
    font-family: "Tinos", "Times New Roman", serif;
    color: var(--gold-text);
  }
  .invite p, .invite h1 { margin: 0; }
  .line {
    position: absolute;
    left: 0;
    width: 100%;
    text-align: center;
    white-space: nowrap;
  }
  .venue-backdrop {
    position: absolute;
    left: 0; top: 500px;
    width: 859px; height: 700px;
    background:
      radial-gradient(ellipse at 50% 25%, rgba(60,140,150,0.55), transparent 60%),
      linear-gradient(180deg, var(--teal-dark) 0%, var(--teal) 35%, #2b2a33 60%, var(--seat-red) 100%);
  }
  .crest-field {
    position: absolute;
    left: 0; top: 0;
    width: 859px; height: 510px;
    background: radial-gradient(ellipse at 50% 45%, #8a1d2b 0%, var(--burgundy) 55%, var(--burgundy-deep) 100%);
  }
  .bands {
    position: absolute;
    left: 0; top: 0;
    width: 859px; height: 1200px;
  }
  .event-date {
    top: 14px;
    font-weight: 700;
    font-size: 42px;
    line-height: 44px;
    letter-spacing: 3px;
    color: var(--maroon-ink);
  }
  .lion-mask {
    position: absolute;
    left: 300px; top: 102px;
    width: 250px; height: 234px;
    border-radius: 45% 45% 30% 30%;
    background: radial-gradient(ellipse at 45% 40%, var(--gold-light) 0%, var(--gold) 45%, var(--gold-deep) 100%);
    opacity: 0.9;
  }
  .hero-title {
    top: 383px;
    font-family: "Cinzel", "Times New Roman", serif;
    font-weight: 500;
    font-size: 46px;
    line-height: 50px;
    color: var(--gold);
  }
  .studio-name {
    top: 510px;
    display: flex;
    justify-content: center;
    align-items: center;
    gap: 10px;
    font-weight: 700;
    font-size: 28px;
    line-height: 34px;
    color: var(--burgundy);
  }
  .studio-name .dot {
    width: 15px; height: 15px;
    border-radius: 50%;
    background: var(--burgundy);
  }
  .welcome { top: 578px; font-size: 32px; line-height: 43px; }
  .show-title { top: 679px; font-size: 40px; line-height: 48px; letter-spacing: 1px; }
  .tagline { top: 767px; font-size: 30px; line-height: 36px; }
  .award-label { top: 828px; font-size: 33px; line-height: 40px; }
  .award-org { top: 875px; font-size: 21px; line-height: 26px; }
  .award-name { top: 907px; font-size: 19px; line-height: 22px; }
  .laurel {
    position: absolute;
    top: 828px;
    width: 65px; height: 117px;
    border-radius: 50% 50% 40% 40%;
    background: linear-gradient(180deg, var(--gold-light), var(--gold));
    opacity: 0.75;
  }
  .laurel-left { left: 186px; }
  .laurel-right { left: 608px; }
  .credit { top: 969px; font-size: 33px; line-height: 32px; }
  .credit-name { top: 1001px; font-size: 27px; font-weight: 700; line-height: 32px; }
  .host { top: 1060px; font-size: 28px; line-height: 34px; }
  .rsvp {
    top: 1154px;
    font-size: 27px;
    line-height: 32px;
    color: var(--maroon-ink);
  }
</style>
</head>
<body>
<main class="invite">
  <div class="venue-backdrop" role="img" aria-label="Theatre auditorium interior with rows of red seats, tinted teal and red"></div>
  <div class="crest-field" role="img" aria-label="Burgundy damask patterned backdrop"></div>

  <svg class="bands" width="859" height="1200" viewBox="0 0 859 1200" aria-hidden="true">
    <defs>
      <linearGradient id="goldSheen" x1="0" y1="0" x2="1" y2="0">
        <stop offset="0" stop-color="#b8893a"/>
        <stop offset="0.3" stop-color="#f2dc98"/>
        <stop offset="0.5" stop-color="#fbefc4"/>
        <stop offset="0.7" stop-color="#f2dc98"/>
        <stop offset="1" stop-color="#b8893a"/>
      </linearGradient>
    </defs>
    <polygon points="0,0 859,0 859,57 680,57 645,97 215,97 179,57 0,57" fill="url(#goldSheen)"/>
    <polygon points="0,455 429,485 859,455 859,508 429,551 0,508" fill="url(#goldSheen)"/>
    <rect x="0" y="1146" width="859" height="54" fill="url(#goldSheen)"/>
  </svg>

  <p class="line event-date">DECEMBER 15, 2015 AT 7 PM</p>
  <div class="lion-mask" role="img" aria-label="Gold winged lion emblem"></div>
  <h1 class="line hero-title">FORSAKING THE HERON</h1>
  <div class="line studio-name"><span class="dot"></span>Larkspur Pictures</div>

  <section class="details">
    <p class="line welcome">You are cordially invited to an innovative<br>theatrical experience.</p>
    <p class="line show-title">FORSAKING THE HERON</p>
    <p class="line tagline">Join us for a glorious night in Renaissance Venice, Italy.</p>
    <div class="laurel laurel-left" role="img" aria-label="Gold laurel branch"></div>
    <div class="laurel laurel-right" role="img" aria-label="Gold laurel branch"></div>
    <p class="line award-label">WINNER</p>
    <p class="line award-org">KRW's “OPEN-HORIZONS”</p>
    <p class="line award-name">Global Scriptwriting Prize</p>
    <p class="line credit">Written and directed by</p>
    <p class="line credit-name">Marla Quistend</p>
    <p class="line host">Hosted by the Gallery Of Harmony<br>4152 East Varlo Ave, Los Angeles, CA 90217</p>
  </section>

  <p class="line rsvp">Please RSVP by December 10 to info@larkspurpics.com</p>
</main>
</body>
</html>
```